Calloway Teaching Placements Business Cards

We need business cards designed for our growing recruitment business.
We have just launched our offices in Sydney Melbourne and have a well established business in Perth. We are a fun young firm that specialise in Early Years Education Recruitment.
Our vision mission values are below
Our Vision:
To be:
the single, nationally recognised leader in the Early Childhood Sector.
a multifaceted organisation with a network of expertly driven facilities in the Early Childhood Sector, acknowledged as an organisation of integrity, innovation, heart and community.

Our Mission:
To provide superior quality recruitment services and solutions to the Early Childhood sector.
We empower our candidates to succeed.
We engage in trusted partnerships with our clients.
We grow our business/network/community, with passion and integrity.

Our Values:

We… are REAL
think: CUSTOMER
find: SOLUTIONS
achieve: RESULTS
enjoy: WHAT WE DO

Our website is www.callowayteaching.com feel free to visit it for inspiration.
Name Felix Harrowby
Title National Director
1300 047 815
0412 736 205
felix@callowayplacements.com
website www.callowayteaching.com

I have attached our current business cards and logo designs to view

Target Market(s)

Recruitment

Industry/Entity Type

Business

Contact Information for Business Card

Name Felix Harrowby
Title National Director
1300 047 815
0412 736 205

Font styles to use
Serif

Requirements
Must have
• Company Values and the cities we have offices in Perth | Sydney | Melbourne
Nice to have
• Our Vision on the card
• Our Vision:
• To be a nationally recognised leader in the Early Childhood Sector.
• A multifaceted organisation with a network of expertly driven facilities in the Early Childhood Sector, acknowledged as an organisation of integrity, innovation, heart and community.

```html
<!DOCTYPE html>
<html lang="en">
<head>
<meta charset="utf-8">
<title>Calloway Teaching Placements – Business Cards</title>
<link rel="stylesheet" href="https://fonts.googleapis.com/css2?family=Open+Sans:wght@400;600;700&family=Noto+Serif:ital,wght@0,400;1,400&display=swap">
<style>
  :root {
    --page-bg: #e9e7e3;
    --card-white: #ffffff;
    --card-shade: #eef0f2;
    --brand-blue: #1a73b8;
    --brand-cyan: #27a9d8;
    --brand-light: #4cc0e6;
    --ink-grey: #5d6670;
    --back-top: #2aa3c9;
    --back-mid: #1d7fb2;
    --back-bottom: #134f86;
    --back-text: #e8f4fa;
    --back-rule: rgba(255,255,255,0.55);
    --icon-tile: #3bbde0;
  }
  * { box-sizing: border-box; margin: 0; padding: 0; }
  html, body { width: 1200px; height: 780px; overflow: hidden; }
  body {
    background: var(--page-bg);
    font-family: "Open Sans", Arial, sans-serif;
    position: relative;
  }
  .card {
    position: absolute;
    top: 235px;
    width: 540px;
    height: 310px;
    border-radius: 3px;
    box-shadow: 0 6px 18px rgba(0,0,0,0.18);
    overflow: hidden;
  }

  /* Front */
  .card-front {
    left: 40px;
    background: radial-gradient(ellipse at 65% 40%, var(--card-white) 40%, var(--card-shade) 100%);
  }
  .brand-block {
    position: absolute;
    left: 34px;
    top: 118px;
    width: 215px;
  }
  .brand-row { display: flex; align-items: center; gap: 12px; }
  .brand-circle {
    width: 62px; height: 62px; flex: none;
    border: 2.5px solid var(--brand-cyan);
    border-radius: 50%;
  }
  .brand-name {
    font-size: 15px;
    font-weight: 600;
    color: var(--brand-blue);
    line-height: 1.2;
    letter-spacing: 0.5px;
    text-transform: uppercase;
  }
  .brand-tagline {
    margin-top: 10px;
    font-size: 10.5px;
    color: var(--brand-blue);
  }
  .front-divider {
    position: absolute;
    left: 262px;
    top: 40px;
    width: 1.5px;
    height: 230px;
    background: var(--brand-light);
  }
  .contact-block {
    position: absolute;
    left: 285px;
    top: 56px;
  }
  .person-name {
    font-size: 22px;
    font-weight: 700;
    color: var(--brand-blue);
    letter-spacing: 0.5px;
    text-transform: uppercase;
  }
  .person-title {
    font-size: 15px;
    color: var(--brand-light);
    margin-top: -2px;
  }
  .contact-list { list-style: none; margin-top: 22px; }
  .contact-list li {
    display: flex; align-items: center; gap: 8px;
    font-size: 12.5px;
    color: var(--ink-grey);
    line-height: 22px;
  }
  .contact-icon {
    width: 15px; height: 15px; flex: none;
    background: var(--brand-cyan);
    border-radius: 2px;
    display: flex; align-items: center; justify-content: center;
  }
  .office-cities {
    margin-top: 14px;
    font-size: 11px;
    font-weight: 600;
    letter-spacing: 0.8px;
    color: var(--brand-cyan);
    text-transform: uppercase;
  }

  /* Back */
  .card-back {
    left: 620px;
    background: linear-gradient(160deg, var(--back-top) 0%, var(--back-mid) 50%, var(--back-bottom) 100%);
    color: var(--back-text);
    padding: 20px 58px 20px 24px;
  }
  .statement-heading {
    font-size: 12px;
    font-weight: 700;
    color: #fff;
  }
  .statement-text {
    font-family: "Noto Serif", Georgia, serif;
    font-style: italic;
    font-size: 10.5px;
    line-height: 1.45;
    margin-top: 2px;
  }
  .statement-rule {
    height: 1px;
    background: var(--back-rule);
    margin: 9px 0 8px;
  }
  .values-grid {
    display: grid;
    grid-template-columns: 150px 1fr;
    row-gap: 1px;
    font-family: "Noto Serif", Georgia, serif;
    font-size: 10.5px;
    margin-top: 4px;
  }
  .values-grid strong { font-family: "Open Sans", Arial, sans-serif; font-weight: 600; letter-spacing: 0.3px; }
  .social-column {
    position: absolute;
    right: 18px;
    bottom: 22px;
    display: flex; flex-direction: column; gap: 6px;
  }
  .social-tile {
    width: 22px; height: 22px;
    background: var(--icon-tile);
    border-radius: 2px;
  }
</style>
</head>
<body>

<section class="card card-front" aria-label="Business card front">
  <div class="brand-block">
    <div class="brand-row">
      <div class="brand-circle"></div>
      <div class="brand-name">Calloway Teaching Placements</div>
    </div>
    <p class="brand-tagline">Bringing quality to education recruitment</p>
  </div>

  <div class="front-divider"></div>

  <div class="contact-block">
    <h1 class="person-name">Felix Harrowby</h1>
    <p class="person-title">National Director</p>
    <ul class="contact-list">
      <li>
        <span class="contact-icon">
          <svg width="10" height="10" viewBox="0 0 10 10"><path d="M2 1h2l1 2.5-1.2.8a5 5 0 0 0 2 2l.8-1.2L9 6v2a1 1 0 0 1-1 1A7 7 0 0 1 1 2a1 1 0 0 1 1-1z" fill="#fff"/></svg>
        </span>1300 047 815
      </li>
      <li>
        <span class="contact-icon">
          <svg width="10" height="10" viewBox="0 0 10 10"><rect x="2.5" y="0.5" width="5" height="9" rx="1" fill="none" stroke="#fff"/><circle cx="5" cy="7.8" r="0.6" fill="#fff"/></svg>
        </span>0412 736 205
      </li>
      <li>
        <span class="contact-icon">
          <svg width="10" height="10" viewBox="0 0 10 10"><rect x="0.5" y="2" width="9" height="6" fill="none" stroke="#fff"/><path d="M0.5 2l4.5 3.5L9.5 2" fill="none" stroke="#fff"/></svg>
        </span>felix@callowayplacements.com
      </li>
      <li>
        <span class="contact-icon">
          <svg width="10" height="10" viewBox="0 0 10 10"><circle cx="5" cy="5" r="4.2" fill="none" stroke="#fff"/><ellipse cx="5" cy="5" rx="1.8" ry="4.2" fill="none" stroke="#fff"/><path d="M0.8 5h8.4" stroke="#fff"/></svg>
        </span>www.callowayteaching.com
      </li>
    </ul>
    <p class="office-cities">Perth | Sydney | Melbourne</p>
  </div>
</section>

<section class="card card-back" aria-label="Business card back">
  <h2 class="statement-heading">Our Vision:</h2>
  <p class="statement-text">the single, nationally recognised leader in the Early Childhood Sector, a multifaceted organisation with a network of expertly driven facilities in the Early Childhood Sector, acknowledged as an organisation of integrity, innovation, heart and community.</p>
  <div class="statement-rule"></div>

  <h2 class="statement-heading">Our Mission:</h2>
  <p class="statement-text">To provide superior quality recruitment services and solutions to the Early Childhood sector.<br>
  We empower our candidates to succeed.<br>
  We engage in trusted partnerships with our clients.<br>
  We grow our business/network/community, with passion and integrity.</p>
  <div class="statement-rule"></div>

  <h2 class="statement-heading">Our Values:</h2>
  <div class="values-grid">
    <span>We… are <strong>REAL</strong></span><span>achieve: <strong>RESULTS</strong></span>
    <span>think: <strong>CUSTOMER</strong></span><span>enjoy: <strong>WHAT WE DO</strong></span>
    <span>find: <strong>SOLUTIONS</strong></span><span></span>
  </div>

  <div class="social-column" aria-hidden="true">
    <span class="social-tile"></span>
    <span class="social-tile"></span>
    <span class="social-tile"></span>
    <span class="social-tile"></span>
    <span class="social-tile"></span>
    <span class="social-tile"></span>
  </div>
</section>

</body>
</html>
```